Business Card Redesign

We would like to redesign our existing business cards.
The new design shall look:
ELEGANT, LUXURY, PROFESSIONAL
Reference:
YOU CAN VISIT WWW.LUMEN-BRIDGE-PARTNERS.EXAMPLE FOR BETTER UNDERSTANDING OF COMPANY STRATEGY AND POSITION
Additional:
CHOSEN CANDIDATE SHALL PROVIDE THE INSTRUCTION OF PRINTING IF ANY THERMAL COVERAGE OR ANY ADDITION IS OFFERED
Industry/Entity Type
Business

```html
<!DOCTYPE html>
<html lang="en">
<head>
<meta charset="utf-8">
<title>Lumen Bridge Partners – Business Card</title>
<link rel="stylesheet" href="https://fonts.googleapis.com/css2?family=Montserrat:wght@400;500;600&display=swap">
<style>
  :root {
    --backdrop: #2b2b2b;
    --card-white: #ffffff;
    --card-gold: #e6a623;
    --brand-blue: #1b5ea8;
    --ink: #2a2a2a;
  }
  * { box-sizing: border-box; margin: 0; padding: 0; }
  html, body { width: 1200px; height: 900px; overflow: hidden; }
  body {
    background: var(--backdrop);
    font-family: "Montserrat", Arial, sans-serif;
    position: relative;
  }
  .card {
    position: absolute;
    top: 292px;
    width: 540px;
    height: 316px;
    border-radius: 28px;
    overflow: hidden;
    background: var(--card-gold);
    box-shadow: 0 14px 30px rgba(0,0,0,0.45);
  }
  .card--front { left: 40px; }
  .card--back { left: 620px; }

  .white-panel {
    position: absolute; top: 0; left: 0; bottom: 0;
    background: var(--card-white);
  }
  .card--front .white-panel { width: 222px; }
  .card--back .white-panel { width: 40px; }

  .blue-stripe {
    position: absolute; top: 0; bottom: 0; width: 8px;
    background: var(--brand-blue);
  }
  .card--front .blue-stripe { left: 222px; }
  .card--back .blue-stripe { left: 40px; }

  .hairline {
    position: absolute; top: 58px; bottom: 58px; width: 2px;
    background: var(--brand-blue);
  }
  .card--front .hairline { left: 206px; }
  .card--back .hairline { left: 28px; }

  .brand {
    position: absolute;
    display: flex; flex-direction: column; align-items: center; gap: 12px;
    color: var(--brand-blue);
    font-weight: 600;
    text-align: center;
    line-height: 1.2;
  }
  .brand__dot {
    border-radius: 50%;
    background: var(--brand-blue);
  }
  .card--front .brand { left: 20px; width: 172px; top: 86px; font-size: 17px; }
  .card--front .brand__dot { width: 78px; height: 78px; }
  .card--back .brand { left: 48px; right: 0; top: 70px; font-size: 22px; }
  .card--back .brand__dot { width: 104px; height: 104px; }

  .contact {
    position: absolute; left: 252px; top: 40px; right: 16px;
    color: var(--ink);
    font-size: 11.5px;
    line-height: 1.45;
  }
  .contact__name { color: var(--brand-blue); font-size: 20px; font-weight: 500; line-height: 1.1; }
  .contact__title { font-size: 11px; margin-bottom: 16px; }
  .contact__block { margin-bottom: 14px; }
  .contact__label { color: var(--brand-blue); }
  .contact__web { color: var(--brand-blue); }

  .back-url {
    position: absolute; left: 48px; right: 0; top: 258px;
    text-align: center;
    color: var(--ink);
    font-size: 17px;
  }
</style>
</head>
<body>
  <section class="card card--front" aria-label="Business card front">
    <div class="white-panel"></div>
    <div class="hairline"></div>
    <div class="blue-stripe"></div>
    <div class="brand">
      <span class="brand__dot"></span>
      <span class="brand__name">Lumen Bridge Partners</span>
    </div>
    <div class="contact">
      <p class="contact__name">Dana Reyes</p>
      <p class="contact__title">PR Consultant</p>
      <div class="contact__block">
        <p>E-mail: dana@lumen-bridge-partners.example</p>
        <p>Mobile: (852) 5550 0142</p>
      </div>
      <div class="contact__block">
        <p class="contact__label">Headquarters (Hong Kong)</p>
        <p>Rm. 1204B, 12/F, Harbourline Tower,<br>18 Lantern Street, Central,<br>Hong Kong</p>
      </div>
      <div>
        <p>Tel: (852) 5550-0178</p>
        <p>Fax: (852) 5550-0179</p>
        <p class="contact__web">www.lumen-bridge-partners.example</p>
      </div>
    </div>
  </section>

  <section class="card card--back" aria-label="Business card back">
    <div class="white-panel"></div>
    <div class="hairline"></div>
    <div class="blue-stripe"></div>
    <div class="brand">
      <span class="brand__dot"></span>
      <span class="brand__name">Lumen Bridge Partners</span>
    </div>
    <p class="back-url">www.lumen-bridge-partners.example</p>
  </section>
</body>
</html>
```